Dorian Felsgrove breaking. Or D. Felsgrove breaking

I break in and train horses, any age any bread of horse, for any disaplin. I need a business card that is simple but effective, in the way of looking professional. I would like a horse on my card, preferably a horse without a rider. I also pre train horse, younge horses that need a bit of riding before they go into serious work, and prepare yearlings for sale.

Reason: This is for my boyfriend, and I really want it to be perfect and impressive!

Target Market(s)

Thoroughbred race horse trainers, horse industrie people.

Industry/Entity Type

Business

Contact Information for Business Card

Dorian Felsgrove horse breaking, "WOLBUNDA" Tallowmere, give your horse the right start to any career. dfels@quillmail.com.au, 0431862097. Horse breaking~pre-training~sale preparation

```html
<!DOCTYPE html>
<html lang="en">
<head>
<meta charset="utf-8">
<title>Dorian Felsgrove – Horse Breaker</title>
<link rel="stylesheet" href="https://fonts.googleapis.com/css2?family=Caladea:wght@400;700&family=Mrs+Saint+Delafield&display=swap">
<style>
  :root {
    --bg-deep: #2c1e17;
    --bg-mid: #45301f;
    --bg-glow: #7a5236;
    --dust: rgba(150, 105, 72, 0.55);
    --tagline: #a5785c;
    --accent: #d9ad8e;
    --accent-soft: #c99a7b;
    --script: #ffffff;
    --rule: #9c7057;
  }
  html, body {
    margin: 0;
    padding: 0;
    width: 1200px;
    height: 702px;
    overflow: hidden;
    background: var(--bg-deep);
  }
  .card {
    position: relative;
    width: 1200px;
    height: 702px;
    overflow: hidden;
    background:
      radial-gradient(ellipse 520px 300px at 840px 200px, var(--bg-glow) 0%, rgba(122,82,54,0) 100%),
      radial-gradient(ellipse 900px 520px at 1000px 60px, #5e3f2a 0%, rgba(94,63,42,0) 100%),
      linear-gradient(160deg, var(--bg-mid) 0%, var(--bg-deep) 70%);
    font-family: "Caladea", Georgia, serif;
  }
  .tagline {
    position: absolute;
    left: 53px;
    top: 40px;
    margin: 0;
    font-size: 38px;
    font-weight: 400;
    letter-spacing: -0.6px;
    white-space: nowrap;
    color: var(--tagline);
  }
  .hero-art {
    position: absolute;
    left: 440px;
    top: 60px;
    width: 700px;
    height: 340px;
    border-radius: 50%;
    background: radial-gradient(ellipse at 55% 50%, var(--dust) 0%, rgba(110,75,50,0.35) 45%, rgba(80,55,38,0) 75%);
  }
  .name {
    position: absolute;
    left: 52px;
    top: 355px;
    margin: 0;
    font-family: "Mrs Saint Delafield", cursive;
    font-weight: 400;
    font-size: 150px;
    line-height: 88px;
    white-space: nowrap;
    color: var(--script);
  }
  .name span { display: block; }
  .role {
    position: absolute;
    right: 655px;
    top: 526px;
    margin: 0;
    font-size: 33px;
    color: var(--accent);
    letter-spacing: 0.5px;
    white-space: nowrap;
  }
  .divider {
    position: absolute;
    left: 572px;
    top: 411px;
    width: 2px;
    height: 212px;
    background: var(--rule);
  }
  .services {
    position: absolute;
    left: 596px;
    top: 414px;
    margin: 0;
    font-size: 35px;
    font-weight: 400;
    letter-spacing: -0.4px;
    white-space: nowrap;
    transform: scaleX(0.92);
    transform-origin: left center;
    color: var(--accent);
  }
  .contacts {
    position: absolute;
    left: 596px;
    top: 466px;
    margin: 0;
    padding: 0;
    list-style: none;
  }
  .contacts li {
    display: flex;
    align-items: center;
    height: 55px;
    font-size: 33px;
    letter-spacing: 1px;
    white-space: nowrap;
    color: var(--accent-soft);
  }
  .contacts svg {
    width: 40px;
    height: 40px;
    margin-right: 29px;
    fill: var(--accent-soft);
    flex: none;
  }
</style>
</head>
<body>
  <main class="card">
    <p class="tagline">“Give your horse the right start to any career”</p>
    <div class="hero-art" role="img" aria-label="Three horses galloping through a cloud of dust"></div>

    <h1 class="name"><span>Dorian</span><span>Felsgrove</span></h1>
    <p class="role">Horse Breaker</p>

    <div class="divider"></div>

    <p class="services">Breaking ~ Pre-Training ~ Sale Preparation</p>
    <ul class="contacts">
      <li>
        <svg viewBox="0 0 24 24" aria-hidden="true"><path d="M6.6 10.8a15.1 15.1 0 0 0 6.6 6.6l2.2-2.2c.3-.3.7-.4 1-.2 1.1.4 2.3.6 3.6.6.6 0 1 .4 1 1V20c0 .6-.4 1-1 1A17 17 0 0 1 3 4c0-.6.4-1 1-1h3.5c.6 0 1 .4 1 1 0 1.3.2 2.5.6 3.6.1.3 0 .7-.2 1z"/></svg>
        043 186 2097
      </li>
      <li>
        <svg viewBox="0 0 24 24" aria-hidden="true"><path d="M3 5h18v14H3zm2 2v.4l7 5 7-5V7zm14 2.8-7 5-7-5V17h14z"/></svg>
        dfels@quillmail.com.au
      </li>
      <li>
        <svg viewBox="0 0 24 24" aria-hidden="true"><path d="M12 3 2 12h3v9h5v-6h4v6h5v-9h3z"/></svg>
        "WOLBUNDA" Tallowmere
      </li>
    </ul>
  </main>
</body>
</html>
```